QuillMark Business Cards

I need a business card designed for QuillMark. To get an idea of what we do please visit https://formvault.example/para-creadores-3

```html
<!DOCTYPE html>
<html lang="en">
<head>
<meta charset="utf-8">
<title>QuillMark Business Card</title>
<link rel="stylesheet" href="https://fonts.googleapis.com/css2?family=Source+Sans+3:wght@400;600;700&display=swap">
<style>
  :root {
    --backdrop: #e3e3e3;
    --amber-light: #eaa233;
    --amber-deep: #d88a1f;
    --accent: #e39423;
    --card-dark: #191d22;
    --decor-dark: #2a2f35;
    --text-light: #e6e7e8;
    --white: #ffffff;
  }
  * { margin: 0; padding: 0; box-sizing: border-box; }
  html, body {
    width: 1200px; height: 960px; overflow: hidden;
    background: var(--backdrop);
    font-family: "Source Sans 3", "Source Sans Pro", sans-serif;
  }
  .canvas { position: relative; width: 1200px; height: 960px; }
  .card {
    position: absolute; left: 297px; width: 611px; height: 349px; overflow: hidden;
  }
  .card-front { top: 108px; }
  .card-back { top: 511px; background: var(--card-dark); }

  .front-pattern {
    position: absolute; inset: 0;
    background:
      radial-gradient(ellipse 60% 80% at 10% 20%, rgba(255,235,200,0.28), transparent 70%),
      linear-gradient(110deg, var(--amber-light) 0%, var(--accent) 50%, var(--amber-deep) 100%);
  }
  .back-decoration {
    position: absolute; left: 290px; top: 0; width: 321px; height: 349px;
    background: radial-gradient(ellipse 50% 55% at 55% 50%, var(--decor-dark) 0%, rgba(42,47,53,0.55) 55%, transparent 100%);
  }

  .brand-dot {
    position: absolute; border-radius: 50%; border: 2px solid var(--white);
  }
  .card-front .brand-dot { left: 122px; top: 132px; width: 64px; height: 64px; }
  .card-back .brand-dot { left: 286px; top: 150px; width: 50px; height: 50px; border-color: var(--accent); }

  .brand-name {
    position: absolute; font-weight: 400; color: var(--white);
    letter-spacing: 0.16em; text-transform: uppercase; line-height: 1;
  }
  .card-front .brand-name { left: 221px; top: 146px; font-size: 36px; }
  .card-back .brand-name { left: 363px; top: 154px; font-size: 27px; }

  .name-marker {
    position: absolute; left: 0; top: 61px; width: 0; height: 0;
    border-top: 14px solid transparent; border-bottom: 14px solid transparent;
    border-left: 22px solid var(--accent);
  }
  .holder-name {
    position: absolute; left: 42px; top: 63px;
    font-size: 20px; font-weight: 700; color: var(--accent); line-height: 1;
  }
  .holder-role {
    position: absolute; left: 42px; top: 89px;
    font-size: 15px; color: var(--text-light); line-height: 1;
  }
  .address {
    position: absolute; left: 42px; top: 190px;
    font-size: 15px; color: var(--text-light); line-height: 20px; font-style: normal;
  }
  .contact-list {
    position: absolute; left: 42px; top: 243px; list-style: none;
    font-size: 15px; color: var(--text-light); line-height: 20.5px;
  }
  .contact-list li { display: flex; align-items: center; gap: 5px; }
  .contact-list svg { width: 14px; height: 14px; flex: none; }
</style>
</head>
<body>
<main class="canvas">
  <section class="card card-front">
    <div class="front-pattern" role="img" aria-label="Amber background with a repeating geometric line pattern"></div>
    <span class="brand-dot"></span>
    <span class="brand-name">QuillMark</span>
  </section>

  <section class="card card-back">
    <div class="back-decoration" role="img" aria-label="Large faint geometric brand decoration"></div>
    <span class="name-marker"></span>
    <h1 class="holder-name">Daniel Whitford</h1>
    <p class="holder-role">Owner</p>

    <span class="brand-dot"></span>
    <span class="brand-name">QuillMark</span>

    <address class="address">418 Harbor Lane<br>Portview, Florida, 33000</address>
    <ul class="contact-list">
      <li>
        <svg viewBox="0 0 16 16" aria-hidden="true"><path fill="#e39423" d="M3.5 1.5l2.4 2.6-1.3 1.8c.8 1.9 2.3 3.4 4.2 4.3l1.8-1.3 2.7 2.3-1.3 2.2C7 13.2 2.8 9 1.4 3.1z"/></svg>
        (555) 014-2277
      </li>
      <li>
        <svg viewBox="0 0 16 16" aria-hidden="true"><rect x="1.5" y="3.5" width="13" height="9" fill="none" stroke="#e39423" stroke-width="1.6"/><path d="M1.5 3.5L8 9l6.5-5.5" fill="none" stroke="#e39423" stroke-width="1.6"/></svg>
        daniel@quillmark.example
      </li>
      <li>
        <svg viewBox="0 0 16 16" aria-hidden="true"><g fill="none" stroke="#e39423" stroke-width="1.4"><circle cx="8" cy="8" r="6.3"/><ellipse cx="8" cy="8" rx="2.8" ry="6.3"/><path d="M1.7 8h12.6M2.6 4.8h10.8M2.6 11.2h10.8"/></g></svg>
        www.quillmark.example
      </li>
    </ul>
  </section>
</main>
</body>
</html>
```